Webdesign für Onlineshop
Zielgruppe
Wir verkaufen in unserem Onlineshop alles zum Thema Wohnen mit dem Schwerpunkt Möbel. Die Hauptzielgruppe ist zwischen 25 und 45 Jahren.
Aufgabenstellung
Wir bevorzugen ein modernes, flaches und aufgeräumtes Design ähnlich wie velm.de / dorano88.de mit dem Fokus auf Preisaggressivität und Rabatte.
- Das Grundlayout muss so bleiben, wie es aktuell ist. Natürlich dürfen einzelne Elemente verschoben / versetzt werden.
- Im Header sollte Platz für eine kleine Werbefläche sein (ähnlich wie der konfigurierbare Kleiderschrank).
- Der Shop basiert auf Magento 1.9.
- Die Rabatte in den Produktdetailseiten müssen genauso aufgebaut sein
- Die Suche sollte in den Header platziert werden und nicht im Menü
- Ein SSL Logo soll im Header platziert weden
- Die Vorteile (Kostenloser Versand, Sicher einkaufen, Kauf auf Rechnung) sollen im Header erscheinen
- Das Design sollte responsive sein
Es wird nur das reine Design ohne Programmierung benötigt.

```html
<!DOCTYPE html>
<html lang="de">
<head>
<meta charset="utf-8">
<title>quellmark3berg – Möbel Online Shop</title>
<link href="https://fonts.googleapis.com/css2?family=Open+Sans:wght@400;600&family=Raleway:wght@300;400&family=Roboto:wght@400;700&display=swap" rel="stylesheet">
<style>
:root{
  --blue:#44a8c4;
  --pink:#c0105a;
  --green:#7cae3c;
  --text:#333;
  --muted:#666;
  --line:#dcdcdc;
  --band:#f0f0f0;
  --foot:#f7f7f7;
}
*{margin:0;padding:0;box-sizing:border-box}
html,body{width:765px;height:1200px;overflow:hidden;background:#fff}
body{position:relative;font-family:"Open Sans",sans-serif;color:var(--text)}
.abs{position:absolute}
.price-old{font-family:"Roboto",sans-serif;font-size:7px;color:#444;text-decoration:line-through}
.price-new{font-family:"Roboto",sans-serif;font-size:13px;color:var(--blue);line-height:16px}
.price-new.sale{color:var(--pink)}
.product{position:absolute;width:130px}
.product .photo{width:130px;height:90px}
.product .name{font-family:"Raleway",sans-serif;font-weight:300;font-size:8.4px;line-height:10.6px;margin:12px 8px 0;height:44px}
.product .prices{margin-left:8px}
.section-title{font-family:"Raleway",sans-serif;font-weight:300;font-size:21px;letter-spacing:.3px}
.arrow-btn{width:30px;height:30px;border:1px solid var(--line);border-radius:50%;display:flex;align-items:center;justify-content:center}
.badge{width:34px;height:34px;border-radius:50%;background:var(--pink);color:#fff;font-family:"Roboto",sans-serif;font-weight:700;font-size:10px;display:flex;align-items:center;justify-content:center}
.seo-heading{left:0;width:765px;text-align:center;font-family:"Raleway",sans-serif;font-weight:300;font-size:18px}
.col{position:absolute}
.col h3{font-family:"Open Sans",sans-serif;font-weight:400;font-size:11px;margin-bottom:5px;color:#222;white-space:nowrap}
.col p{font-size:6.9px;line-height:9.7px;color:#333;margin-bottom:6px}
.newsletter{left:0;top:768px;width:765px;height:118px;background:var(--band)}
.newsletter .lead{position:absolute;left:178px;top:23px;font-family:"Raleway",sans-serif;font-weight:300;font-size:10.5px;line-height:14.5px;color:#555}
.newsletter .field{position:absolute;left:178px;top:70px;width:279px;height:28px;background:#fff;border:1px solid var(--line);font-size:6.5px;color:#555;padding:9px 12px}
.newsletter .cta{position:absolute;left:456px;top:70px;width:133px;height:28px;background:var(--blue);color:#fff;font-family:"Roboto",sans-serif;font-weight:700;font-size:10px;display:flex;align-items:center;justify-content:center}
.voucher{position:absolute;left:502px;top:-10px;width:72px;height:70px;background:linear-gradient(135deg,#f0f0f0 20%,#8bbd4a 45%,#6f9f33 80%,#f0f0f0 81%)}
.perk{position:absolute;top:909px;width:179px;height:55px;border:1px solid var(--line);overflow:hidden}
.perk h4{position:absolute;left:11px;top:10px;z-index:2;white-space:nowrap;font-family:"Raleway",sans-serif;font-weight:400;font-size:11px;color:var(--blue)}
.perk p{position:absolute;left:11px;top:29px;z-index:2;font-size:5.5px;line-height:8.3px;color:#333}
.perk .visual{position:absolute;right:4px;top:4px;width:52px;height:50px;border-radius:3px;z-index:1}
.pay-band{left:0;top:980px;width:765px;height:37px;background:var(--blue);display:flex;align-items:center;justify-content:center;gap:18px}
.pay-band .method{font-family:"Open Sans",sans-serif;font-weight:600;font-size:8.5px;color:#e8f5f9}
.pay-band .tag{font-family:"Open Sans",sans-serif;font-weight:600;font-size:4.5px;color:var(--blue);background:#d6eef5;padding:2px 5px}
.footer-col{position:absolute;top:1040px}
.footer-col h5{font-family:"Open Sans",sans-serif;font-weight:400;font-size:7.5px;color:#222;margin-bottom:9px}
.footer-col li{list-style:none;font-size:5.6px;line-height:11.6px;color:#333}
.footer-col .sub{font-family:"Roboto",sans-serif;font-weight:700;font-size:6px;color:var(--blue);margin-top:4px}
.footer-col .small{font-size:5.5px;line-height:8.7px;color:#333}
.social{width:19px;height:19px;border-radius:50%;background:var(--blue);display:inline-block;margin-right:5px}
.divider{position:absolute;left:308px;top:1033px;width:1px;height:102px;background:var(--line)}
.seal{position:absolute;border-radius:50%;background:linear-gradient(135deg,#e9c23a,#c9951c)}
.rating{position:absolute;left:560px;top:1030px;width:97px;height:47px;border:1px solid var(--line)}
.rating .seal{left:8px;top:6px;width:34px;height:34px;background:#3b3b3b}
.rating .score{position:absolute;left:56px;top:6px;font-family:"Roboto",sans-serif;font-size:10px;color:var(--blue)}
.rating .score span{color:#333;font-size:9px}
.rating .stars{position:absolute;left:53px;top:19px;font-size:6px;color:var(--blue);letter-spacing:.5px}
.rating .verdict{position:absolute;left:57px;top:30px;font-size:6.5px;color:#333}
.legal-note{position:absolute;left:560px;top:1098px;width:95px;font-size:4.3px;line-height:6.7px;color:#333}
.bottom-bar{left:0;top:1163px;width:765px;height:37px;background:var(--foot);text-align:center;font-size:5px;color:#888;padding-top:17px}
</style>
</head>
<body>

<div class="abs" style="left:113px;top:-4px;font-family:Raleway,sans-serif;font-weight:300;font-size:8.4px">braun</div>
<div class="abs" style="left:113px;top:18px"><div class="price-old">999,00 €</div><div class="price-new sale">575,10 €</div></div>
<div class="abs" style="left:253px;top:18px"><div class="price-old">999,00 €</div><div class="price-new">575,10 €</div></div>
<div class="abs" style="left:393px;top:18px"><div class="price-old">999,00 €</div><div class="price-new">575,10 €</div></div>
<div class="abs" style="left:533px;top:18px"><div class="price-old">999,00 €</div><div class="price-new">575,10 €</div></div>

<h2 class="abs section-title" style="left:102px;top:89px">BELIEBTE ARTIKEL</h2>
<div class="abs arrow-btn" style="left:585px;top:91px"><svg width="10" height="8" viewBox="0 0 10 8"><path d="M9 4H1M4 1L1 4l3 3" fill="none" stroke="#555" stroke-width="1"/></svg></div>
<div class="abs arrow-btn" style="left:623px;top:91px"><svg width="10" height="8" viewBox="0 0 10 8"><path d="M1 4h8M6 1l3 3-3 3" fill="none" stroke="#555" stroke-width="1"/></svg></div>

<div class="product" style="left:103px;top:132px">
  <div class="photo" role="img" aria-label="Nachttisch aus hellem Holz neben einem Holzbett" style="background:linear-gradient(135deg,#a9ad8c,#c08a4c 55%,#8a5a2a)"></div>
  <div class="name">Wohnlandschaft, in Mikrofaser Vintage-Look braun</div>
  <div class="prices"><div class="price-old">999,00 €</div><div class="price-new">575,10 €</div></div>
</div>
<div class="product" style="left:243px;top:132px">
  <div class="photo" role="img" aria-label="Graues Boxspringbett mit Decke im Schlafzimmer" style="background:linear-gradient(160deg,#d8d6d2,#b9b9b6 55%,#8a6b52)"></div>
  <div class="name">Boxspringbett schwarz, Feinstrukturstoff</div>
  <div class="prices"><div class="price-old">999,00 €</div><div class="price-new">575,10 €</div></div>
</div>
<div class="product" style="left:383px;top:132px">
  <div class="photo" role="img" aria-label="Kleiderschrank in Eiche und Grau mit Spiegeltüren" style="background:linear-gradient(90deg,#e8e6e0,#c9a878 30%,#5a5650 55%,#c9a878 80%,#4fc0c8)"></div>
  <div class="name">Boxspringbett schwarz, Feinstrukturstoff</div>
  <div class="prices"><div class="price-old">999,00 €</div><div class="price-new sale">575,10 €</div></div>
</div>
<div class="badge abs" style="left:379px;top:128px">-36%</div>
<div class="product" style="left:523px;top:132px">
  <div class="photo" role="img" aria-label="Weißes Bett mit roter Decke und Nachtkommode" style="background:linear-gradient(135deg,#d9d9d9,#3c3f44 40%,#f2f2f2 60%,#b01822)"></div>
  <div class="name">Boxspringbett schwarz, Feinstrukturstoff</div>
  <div class="prices"><div class="price-old">999,00 €</div><div class="price-new">575,10 €</div></div>
</div>

<h2 class="abs seo-heading" style="top:345px">Möbel im Online Shop von quellmark3berg</h2>

<div class="col" style="left:108px;top:392px;width:264px">
  <h3>Immer modern, hochwertig &amp; günstig</h3>
  <p>Der Name des Online Shops quellmark3berg ist Programm: Hier finden Sie stilvolle Möbel, Accessoires und weiteres Zubehör für das Leben in den eigenen vier Wänden. Überzeugen Sie sich selbst - entdecken Sie unser großes Sortiment an modernen Möbelstücken und richten Sie Ihre Wohnung stilvoll ein!</p>
  <h3 style="margin-top:12px">So finden Sie Ihre Traummöbel</h3>
  <p>Vergeuden Sie keine Zeit mehr mit der mühsamen Suche im lokalen Möbelhaus. Im Online Shop von quellmark3berg finden Sie zu jeder Zeit und auf schnelle Weise moderne Möbel zum günstigen Preis. Vom Wohnzimmer über die Küche bis hin zum Jugendzimmer, ob Badmöbel oder Esszimmermöbel – ganz gleich, für welchen Wohnraum Sie eine neue Einrichtung suchen, mit der übersichtlichen Navigation und dem praktischen Suchfilter finden Sie Möbelstücke, die Ihren Anforderungen entsprechen. Wählen Sie einfach Material, Farbe, Maße und Ihr gewünschtes Budget aus. In Sekundenschnelle erhalten Sie eine breite Auswahl an Möbeln.</p>
  <h3 style="margin-top:17px">Möbel direkt vom Hersteller</h3>
  <p>In unserem Shop können Sie moderne Wohnwände, Polstermöbel, Schränke und weitere Wohnzimmermöbel günstig online bestellen. Unser Produktportfolio enthält Möbel direkt vom Hersteller, wodurch wir dem Kunden unsere Artikel zu Top Konditionen anbieten können. Außerdem profitieren Sie von einer hochwertigen Qualität, einem trendigen Design und dem ausgezeichneten Service von quellmark3berg.</p>
  <h3 style="margin-top:17px;font-size:10.5px;letter-spacing:-.1px">Unser großes Möbel Angebot - Entdecken Sie die Vielfalt</h3>
  <p>Es gibt eine Vielzahl an Maßen, Farben und Materialien, die in der Summe ein unterschiedliches Design hervorrufen. Dabei hat jeder Mensch seinen ganz eigenen Geschmack. Damit wir auch Ihre Vorliebe in Sachen Wohnungseinrichtung treffen, finden Sie in unserem Online Shop ein großes Angebot an Möbeln in unterschiedlichen Stilrichtungen.</p>
</div>

<div class="col" style="left:388px;top:393px;width:264px">
  <p>Sie suchen nach einem bequemen Fernseh-Sessel in einem coolen Design? Dann empfehlen wir Ihnen unseren Relax Sessel im schwarzen Kunstleder und mit einer verstellbaren Rückenlehne. Ein kleiner Hocker ist ebenso in der Lieferung enthalten und sorgt für zusätzlichen Liegekomfort. Selbstverständlich bieten wir Ihnen passend zu diesem Möbelstück Sideboards, Stühle, Wandregale, Sofas und Co. an. Mit quellmark3berg können Sie Ihr Wohnzimmer in einem einheitlichen Stil einrichten.</p>
  <p>Auch für das Schlafzimmer finden Sie eine Vielzahl an unterschiedlichen Betten, Kleiderschränken, Nachttischen sowei weitere Schlafzimmermöbel. Überzeugen Sie sich selbst und bestellen Sie Ihre gewünschten Möbel günstig in unserem Online Shop!</p>
  <h3 style="margin-top:14px">Möbel für Babys und Kinder</h3>
  <p style="line-height:11.9px">In unserm Shop finden Sie eine große Auswahl an Kindermöbeln. Wir bieten Ihnen komplette Babyzimmer und Jugendzimmer Sets, mit denen Sie das Zimmer Ihres Kindes im handumdrehen wunschgerecht und günstig einrichten. Dabei legen wir hohe Maßstäbe an die Qualität der Möbel und stehen Ihnen mit unserem kompetenten Service gerne beratend zur Seite.</p>
  <h3 style="margin-top:14px">Unser Service</h3>
  <p>Bei Fragen stehen wir Ihnen gerne zur Verfügung. Schreiben Sie uns einfach eine E-Mail oder kontaktieren Sie unsere Service-Mitarbeiter telefonisch. Wir helfen Ihnen gerne bei der Auswahl Ihrer Wunschmöbel.</p>
  <p>Neben unserer kompetenten Beratung profitieren Sie auch von unserem zuverlässigen Lieferservice ohne Aufpreis.</p>
  <p>Außerdem bieten wir Ihnen mehrere zuverlässige Zahlarten an. Sie entscheiden, ob Sie per Banküberweisung, Zahlfix, Nachnahme, Kreditkarte, Rechnungskauf oder per Finanzierung zahlen wollen.</p>
</div>

<section class="abs newsletter">
  <p class="lead">Kostenlosen Newsletter abonnieren, von zahlreichen<br>Aktionen profitieren und einen kostenlosen Einkaufsgutschein</p>
  <div class="field">Ihre E-mail adresse</div>
  <div class="cta">JETZT SICHERN!</div>
  <div class="voucher" role="img" aria-label="Grünes Anhängeschild mit 5 Euro Gutschein"></div>
</section>

<div class="perk" style="left:108px">
  <h4>Versandkostenfrei</h4>
  <p>Ohne Aufpreis.<br>Nutzen Sie unser Angebot!</p>
  <div class="visual" role="img" aria-label="Weißer Lieferwagen" style="background:linear-gradient(180deg,#fff 20%,#e6e6e6 70%,#555)"></div>
</div>
<div class="perk" style="left:294px">
  <h4>0489 / 27 61 54 30</h4>
  <p>Ohne Aufpreis.<br>Nutzen Sie unser Angebot!</p>
  <div class="visual" role="img" aria-label="Service-Mitarbeiterin mit Headset" style="background:linear-gradient(180deg,#f0d9c4,#f4f4f4)"></div>
</div>
<div class="perk" style="left:480px">
  <h4>Unschlagbaren Preisen</h4>
  <p>Direkt vom Hersteller</p>
  <div class="visual" role="img" aria-label="Hellblaues Sparschwein mit Münze" style="width:40px;background:radial-gradient(circle at 50% 65%,#7fd3e4,#fff 70%)"></div>
</div>

<div class="abs pay-band">
  <span class="method">Zahlfix</span>
  <span class="method">Mondakarte</span>
  <span class="method">Direktweg</span>
  <span class="method">Kartora</span>
  <span class="method">Rechnung</span>
  <span class="tag">-3% BANKÜBERWEISUNG</span>
  <span class="tag">FINANZIERUNG</span>
  <span class="tag">NAHNAHME</span>
</div>

<div class="footer-col" style="left:107px">
  <h5>Kundenservice</h5>
  <ul><li>Zahlungsarten</li><li>Lieferung</li><li>AGB</li><li>Widerrufsrecht</li><li>Datenschutz</li><li>Katalog</li><li>Blog</li></ul>
</div>
<div class="footer-col" style="left:183px">
  <h5>Über uns</h5>
  <ul><li>Über uns</li><li>Kontakt</li><li>Impressum</li></ul>
</div>
<div class="footer-col" style="left:240px">
  <h5>Folge uns auf</h5>
  <span class="social"></span><span class="social"></span>
</div>
<div class="divider"></div>
<div class="footer-col" style="left:325px">
  <h5>Einfach und sicher</h5>
  <div class="sub">Bestellvorgang</div>
  <div class="small">Schnell, übersichtlich und<br>mit SSL-Datenschutz</div>
  <div class="sub" style="margin-top:12px">Lieferung</div>
  <div class="small">Kostenlose Lieferung<br>innerhalb Deutschland.</div>
</div>
<div class="seal" style="left:517px;top:1034px;width:37px;height:37px"></div>
<div class="rating">
  <div class="seal"></div>
  <div class="score">4.25<span>/5</span></div>
  <div class="stars">★★★★★</div>
  <div class="verdict">Sehr gut</div>
</div>
<div class="seal" style="left:517px;top:1092px;width:37px;height:37px"></div>
<p class="legal-note">Eine kontinuierliche Überwachung durch spezialisierte Anwälte stellt sicher, dass unsere Kunden vollständig und korrekt über ihre Rechte aufgeklärt werden.</p>

<div class="abs bottom-bar">Preisangaben inkl. gesetzl. MwSt. und zzgl. Service- und Versandkosten</div>

</body>
</html>
```